Web site - 5-8 page

We are a small, fresh pasta business called The Noodle Baroness located in suburbs of Sacramento, CA. We sell our pasta, ravioli, meatballs and sauce at farmer's markets, events, and soon in our café & marketplace. (Jan 2014) . We also provide catering services. The site needs to communicate FRESH, local, no preservatives, artisan quality pasta. We offer vegetarian, vegan and gluten free products as well.

We would like a web site using our logos and colors to feature what we do, and where people can come buy it. A page to our standard take and make items/menu, our seasonal take and make menu, our catering menu, our new hot food café menu.

We want a page that we can update with "Where can you find The Noodle Baroness"
A "specials page" and a page they can order from that they choose the location to pick it up or in the delivery area we deliver to them.
A page with photo's and referrals, testimony, comments, about us, etc. Maybe a page for recipes.
We need to update the events/find us page all the time, weekly, so it needs to be easy for us to go in and do that. We are Window's (not MAC) users if that makes a difference or not, not sure.

Ideally, the same person(s) that make the website would also do a separate project creating our catering and hot food menu brochure/layout and recipe cards
Updates

I would like to see the landing page have the pasta shapes/sizes element that is found in the refrigerator wrap, the wrap on the trailer, and the menu - see photo and uploads. It's used as a banner or as a background, bright green.

                                   

 

Would like visitors to be able to "like" me or follow me from my web page. A button or a link?

                                        http://www.brightlarder-example.com/our-food/

Really like the layout of this site. More grocery oriented than café, but we are a take and make marketplace as well as a Panini salads and hot pasta menu for lunch.

Please add Café + Marketplace to headers. Our logo is good but we are now adding a café element and a fresh marketplace, se we need to communicate what we are/what we do. We think adding Café + Marketplace as a descriptor will help. Any ideas, feel free to put your own spin on it. Thank you!!

The designs are good...thanks to everyone!

Target Market(s)

#1, busy mom's, busy family's (FAST, Economical meals, no preservatives, local food)
#2 24-34 yr olds that want fresh, vegetarian, vegan or gluten free meal options (no preservatives, local food)
#3 Fresh pasta lovers - any age. The enjoyment of quality fresh pasta and a good meal experience sharing it with friends and family

Industry/Entity Type

Catering

Font styles to use
Other font styles liked:
• EideticNeoRegular, duffy

Colors
9bcb3c
f78f20
eb1f27

Requirements
Must have
• Address, phone, name, logo, colors
Fresh pasta, ravioli, sauce and meatballs in take and make convenient packages. Stress fresh, preservative free, local ingredients, cooks in 45 SECONDS to 3.5 minutes depending on the pasta cut.
FAST meal
Where to find us page - upcoming events
A "specials" page
A page for recipe, how to cook our pasta, how to freeze and store fresh pasta,
How to order online page
Nice to have
• Testimony, links to Chatterbook, chirpnet, etc. Place for photo's of product, recent events, customer comments on how they used the product to create their recipe.
Should not have
• No stock photo's of tomato's, no dried pasta images, no Italian flags. No cheesy old world Italian loo or feel. Think fresh, modern, FAST!

```html
<!DOCTYPE html>
<html lang="en">
<head>
<meta charset="utf-8">
<title>The Noodle Baroness · Café + Marketplace · Catering Services</title>
<link href="https://fonts.googleapis.com/css2?family=Arimo:ital,wght@0,400;0,700;1,400;1,700&family=Merriweather:wght@700&display=swap" rel="stylesheet">
<style>
:root{
  --lime:#a6c700;
  --lime-light:#e6ef8a;
  --olive:#6d8a00;
  --olive-dark:#4f6400;
  --green-text:#3f5a00;
  --red:#ef1b1b;
  --red-dark:#c40e0e;
  --white:#ffffff;
  --panel:#f6f6f4;
  --grey-line:#8fa26a;
  --body-text:#3c5200;
}
*{margin:0;padding:0;box-sizing:border-box}
html,body{width:1125px;height:1200px;overflow:hidden;background:var(--white)}
body{position:relative;font-family:"Arimo",Arial,sans-serif;color:var(--body-text)}
.abs{position:absolute}

/* header */
.top-band{left:0;top:0;width:1125px;height:127px;background:var(--lime)}
.zigzag{left:0;width:1125px;height:10px}
.brand{left:192px;top:30px;width:178px;height:160px;text-align:center}
.brand-name{font-weight:700;font-size:27px;line-height:30px;color:var(--red);padding-top:18px}
.brand-square{display:inline-block;width:14px;height:14px;background:var(--red);margin-bottom:6px}
.brand-tag{position:absolute;left:0;right:0;top:142px;font-size:17px;color:#333}
.site-title{left:400px;top:56px;font-size:30px;font-weight:700;color:var(--olive)}
.site-sub{left:400px;top:90px;font-size:14px;color:var(--olive)}
.callbox{left:745px;top:0;width:192px;height:115px;background:var(--red);border-radius:0 0 6px 6px;color:var(--white);padding:15px 0 0 26px}
.callbox .label{font-size:12px}
.callbox .phone{font-size:24px;font-weight:700;line-height:28px}
.callbox .addr{font-size:11.5px;line-height:14px;margin-top:3px}
.callbox .hours{font-size:11.5px;font-weight:700;margin-top:5px}

.main-nav{left:356px;top:148px;width:511px;height:38px;background:var(--red);border-radius:6px 4px 14px 10px;border-bottom:3px solid var(--red-dark);display:flex;align-items:center;padding-left:18px}
.main-nav a{color:var(--white);text-decoration:none;font-size:12.5px;padding:0 15px;border-left:2px dotted var(--red-dark)}
.main-nav a:first-child{border-left:none;padding-left:0}
.main-nav a.active{font-weight:700}
.follow{left:881px;top:140px;font-size:11.5px;color:var(--olive)}
.social{display:flex;gap:6px;margin-top:5px}
.social span{display:flex;align-items:center;font-size:9px;color:var(--olive-dark)}
.social i{display:inline-block;width:12px;height:12px;background:var(--olive);border-radius:2px;margin-right:3px}

/* hero */
.hero{left:188px;top:197px;width:749px;height:342px;border:3px solid var(--lime);border-radius:6px;background:var(--white);overflow:hidden}
.hero-photo{position:absolute;left:4px;top:4px;width:736px;height:292px;background:linear-gradient(100deg,#d79a5a 0%,#f1d9b8 35%,#fbf4ea 60%,#f6e2cc 80%,#e86a2a 100%)}
.badge{position:absolute;left:445px;top:38px;width:138px;height:138px}
.badge-text{position:absolute;left:445px;top:78px;width:138px;text-align:center;color:var(--olive-dark);font-weight:700;line-height:30px}
.badge-text b{font-size:31px;display:block}
.badge-text small{font-size:13px;display:block;line-height:10px;font-weight:400}
.hero-claim{position:absolute;left:590px;top:70px;width:150px;text-align:right;color:var(--olive)}
.hero-claim .line{font-size:15px;line-height:16px}
.hero-claim .big{font-size:26px;font-weight:700;line-height:30px}
.order-bar{position:absolute;left:4px;top:295px;width:736px;height:40px;display:flex}
.order-label{width:274px;background:var(--red);color:var(--white);padding:6px 0 0 24px}
.order-label strong{font-size:17px;display:block;line-height:17px}
.order-label span{font-size:10px;font-weight:700}
.order-fields{width:339px;background:var(--lime-light);display:flex;align-items:center;padding-left:15px;gap:10px}
.select{height:24px;background:var(--white);border:1px solid #d6d6c4;border-radius:3px;font-size:10.5px;color:#888;display:flex;align-items:center;padding-left:9px;position:relative}
.select::after{content:"";position:absolute;right:0;top:0;width:30px;height:22px;border-left:1px solid #ddd;background:linear-gradient(var(--white),#eee)}
.select svg{position:absolute;right:10px;top:6px;z-index:1}
.order-btn{flex:1;background:var(--olive);color:var(--white);font-family:"Merriweather",Georgia,serif;font-size:15px;display:flex;align-items:center;justify-content:center;border:2px solid var(--lime-light)}

/* content */
.page-title{left:215px;top:576px;font-size:28px;font-weight:700;color:var(--olive)}
.page-sub{left:215px;top:607px;font-size:14px;color:var(--olive);display:flex;align-items:center}
.page-sub b{font-weight:700}
.page-sub em{font-style:normal;font-size:11.5px;border-left:1px solid var(--olive);margin-left:10px;padding-left:10px;line-height:18px}
.body-copy{left:217px;top:656px;width:421px;font-size:11.5px;line-height:15.6px;text-align:justify;color:var(--body-text)}
.body-copy p{margin-bottom:15.6px}

.side-head{left:685px;top:586px;width:252px;text-align:center;color:var(--olive);line-height:22px}
.side-head .l1{font-size:19px}
.side-head .l2{font-size:16px;font-weight:700}
.finder{left:685px;top:642px;width:252px;height:319px;background:var(--panel);border:1px solid var(--grey-line);border-radius:0 0 4px 4px;padding:35px 0 0 14px}
.finder h4{font-size:14px;font-style:italic;font-weight:700;color:var(--olive-dark);padding-left:20px;position:relative}
.finder h4 svg{position:absolute;left:0;top:2px}
.finder .kicker{font-size:8.5px;font-weight:700;padding-left:20px;display:block;color:var(--olive-dark)}
.finder ul{list-style:none;padding-left:29px;margin:6px 0 24px}
.finder li{font-size:11.5px;line-height:18.8px;color:var(--body-text)}

/* footer */
.footer{left:0;top:999px;width:1125px;height:201px;background:var(--lime)}
.mascot{left:183px;top:1022px;width:150px;height:164px;border-radius:8px;background:linear-gradient(160deg,#94b500,#5c7a00)}
.foot-nav{left:361px;top:1020px;width:548px;display:flex;justify-content:space-between;font-size:11.5px;color:var(--green-text);padding:0 16px;padding-bottom:13px;border-bottom:1px solid #d9e89a}
.foot-call{left:374px;top:1078px;color:var(--green-text)}
.foot-call .label{font-size:11.5px}
.foot-call .phone{font-size:24px;font-weight:700;line-height:26px}
.foot-call .addr{font-size:11.5px;line-height:14px;margin-top:2px}
.foot-call .hours{font-size:11.5px;font-weight:700}
.view-map{left:367px;top:1164px;width:85px;height:18px;background:var(--lime-light);font-size:11px;font-style:italic;color:var(--green-text);padding:2px 0 0 8px}
.news{left:581px;top:1071px;color:var(--green-text)}
.news h5{font-size:13.5px;font-style:italic;font-weight:700}
.news p{font-size:11px}
.email{left:581px;top:1103px;width:235px;height:32px;background:var(--white);border:1px solid #cddc88;border-radius:3px;display:flex;align-items:center;font-size:12px;color:#aaa}
.email .ico{width:34px;height:100%;border-right:1px solid #ddd;display:flex;align-items:center;justify-content:center}
.email span{padding-left:10px}
.subscribe{left:581px;top:1142px;width:146px;height:28px;background:var(--olive);border:2px solid var(--lime-light);border-radius:3px;color:var(--white);font-size:13px;display:flex;align-items:center;justify-content:center}
.copyright{left:581px;top:1180px;font-size:10px;color:var(--green-text)}
.foot-follow{left:843px;top:1087px;font-size:11px;color:var(--green-text)}
.foot-follow .social i{background:var(--olive-dark)}
</style>
</head>
<body>

<header>
  <div class="abs top-band"></div>
  <svg class="abs zigzag" style="top:126px" viewBox="0 0 1125 10" preserveAspectRatio="none" aria-hidden="true">
    <defs><pattern id="zz" width="10" height="10" patternUnits="userSpaceOnUse"><polygon points="0,0 10,0 5,8" fill="#a6c700"/></pattern></defs>
    <rect width="1125" height="10" fill="url(#zz)"/>
  </svg>

  <div class="abs brand">
    <span class="brand-square"></span>
    <div class="brand-name">The Noodle Baroness</div>
    <div class="brand-tag">Freshly Simple</div>
  </div>

  <div class="abs site-title">Café + Marketplace</div>
  <div class="abs site-sub">Preservative Free, Local Ingredients, Fast Meal</div>

  <div class="abs callbox">
    <div class="label">Call or Text to Order</div>
    <div class="phone">916 555 0148</div>
    <div class="addr">4820 Amberline Way #210<br>Rancho Verde, CA 95600</div>
    <div class="hours">8:00am to 4:00pm</div>
  </div>

  <nav class="abs main-nav">
    <a href="#">Home</a><a href="#" class="active">Menu</a><a href="#">Specials</a><a href="#">Catering Services</a><a href="#">Cooking Classes</a><a href="#">Contact Us</a>
  </nav>

  <div class="abs follow">Follow us:
    <div class="social"><span><i></i>Chatterbook</span></div>
    <div class="social"><span><i></i>chirpnet</span></div>
  </div>
</header>

<section class="abs hero">
  <div class="hero-photo" role="img" aria-label="Photo of a couple cooking fresh vegetables in a kitchen, with a plate of fusilli pasta in tomato sauce"></div>
  <svg class="badge" viewBox="0 0 138 138" aria-hidden="true">
    <circle cx="69" cy="69" r="68" fill="#b9d400"/>
    <circle cx="69" cy="69" r="58" fill="#e6ef8a" stroke="#fff" stroke-width="3"/>
  </svg>
  <div class="badge-text"><b>TAKE</b><small>and</small><b>MAKE</b></div>
  <div class="hero-claim">
    <svg width="16" height="16" viewBox="0 0 16 16" aria-hidden="true"><circle cx="8" cy="8" r="7" fill="none" stroke="#6d8a00" stroke-width="1.2"/><path d="M8 3v5l-3 2" fill="none" stroke="#6d8a00" stroke-width="1.2"/></svg>
    <div class="line">Dinner in 10 Min!</div>
    <div class="line">No Preservatives!</div>
    <div class="big">Eat Local!</div>
  </div>
  <div class="order-bar">
    <div class="order-label"><strong>Order Here</strong><span>Fresh Pasta, Ravioli, Gnocchi, Tortellini, Sauce.</span></div>
    <div class="order-fields">
      <div class="select" style="width:134px">Choose your Pasta<svg width="8" height="11" viewBox="0 0 8 11"><path d="M4 0l4 4H0zM4 11L0 7h8z" fill="#666"/></svg></div>
      <div class="select" style="width:64px">Oz.<svg width="8" height="11" viewBox="0 0 8 11"><path d="M4 0l4 4H0zM4 11L0 7h8z" fill="#666"/></svg></div>
      <div class="select" style="width:84px">Sauce<svg width="8" height="11" viewBox="0 0 8 11"><path d="M4 0l4 4H0zM4 11L0 7h8z" fill="#666"/></svg></div>
    </div>
    <div class="order-btn">Order!</div>
  </div>
</section>

<main>
  <h1 class="abs page-title">Catering Services</h1>
  <div class="abs page-sub"><b>Café + Marketplace</b><em>Preservative Free, Local Ingredients, Fast Meal</em></div>
  <div class="abs body-copy">
    <p>Lorem ipsum dolor sit amet, at postea facilisis eum, eam nemore disputationi cu. Iisque equidem nam ut. Vidit exerci nam te, ut pri modo volutpat intellegebat, vide movet omittantur sed in. In est viris patrioque. Pri ad sententiae quaerendum. Dicant dicunt veritus eu vis. Duo ad similique democritum, an dicit vocent ceteros usu. Tation latine suscipit eam ne. Assum veritus aliquando est cu. Duo ad similique demotcritum, an dicit.</p>
    <p>Ad duo abhorreant moderatius. Nam ex fuisset verterem, saepe primis intellegam sit no, vim quod dolor ei. Fugit nobis invidunt ei quo, posse evertitur moderatius no nec. Vm quod dolor ei. Fugit nobis invid.</p>
    <p>Lorem ipsum dolor sit amet, at postea facilisis eum, eam nemore disputationi cu. Iisque equidem nam ut. Vidit exerci nam te, ut pri modo volutpat intellegebat, vide movet omittantur sed in. In est viris patrioque. Pri ad sententiae quaerendum. Dicant dicunt veritus eu vis. Duo ad similique democritum, an dicit vocent ceteros usu. Tation latine suscipit eam ne. Assum veritus aliquando est cu. Duo ad similique demotcritum, an dicit.</p>
  </div>

  <div class="abs side-head"><div class="l1">Where can you find</div><div class="l2">The Noodle Baroness</div></div>
  <aside class="abs finder">
    <span class="kicker">WEDNESDAY</span>
    <h4><svg width="12" height="12" viewBox="0 0 12 12"><rect x="0.5" y="1.5" width="11" height="10" fill="none" stroke="#777"/><path d="M1 4h10M3 6h2M7 6h2M3 8.5h2M7 8.5h2" stroke="#777"/></svg>Market Schedule</h4>
    <ul><li>Raleigh Downtown - 10:00am -2:00pm</li><li>Durham - 3:30pm - 6:30pm</li></ul>
    <h4><svg width="12" height="12" viewBox="0 0 12 12"><rect x="0.5" y="1.5" width="11" height="10" fill="none" stroke="#777"/><path d="M1 4h10M3 6h2M7 6h2M3 8.5h2M7 8.5h2" stroke="#777"/></svg>Stores</h4>
    <ul><li>Willow Lane Market Carrboro</li><li>Willow Lane Market Hillsborough</li><li>Willow Lane Market Chapel Hill</li><li>Rowan's Butcher &amp; Sweet Shop</li></ul>
    <h4><svg width="12" height="12" viewBox="0 0 12 12"><rect x="0.5" y="1.5" width="11" height="10" fill="none" stroke="#777"/><path d="M1 4h10M3 6h2M7 6h2M3 8.5h2M7 8.5h2" stroke="#777"/></svg>Restaurants</h4>
    <ul><li>Silver Spoon</li><li>Hillcrest</li></ul>
  </aside>
</main>

<footer>
  <div class="abs footer"></div>
  <svg class="abs zigzag" style="top:990px" viewBox="0 0 1125 10" preserveAspectRatio="none" aria-hidden="true">
    <defs><pattern id="zz2" width="10" height="10" patternUnits="userSpaceOnUse"><polygon points="0,10 10,10 5,2" fill="#a6c700"/></pattern></defs>
    <rect width="1125" height="10" fill="url(#zz2)"/>
  </svg>
  <div class="abs mascot" role="img" aria-label="Illustration of the brand's crowned mascot holding a fork and knife, with the slogan Long live the queen"></div>
  <nav class="abs foot-nav"><span>Home</span><span>Menu</span><span>Specials</span><span>Catering Services</span><span>Cooking Classes</span><span>Contact Us</span></nav>
  <div class="abs foot-call">
    <div class="label">Call or Text to Order</div>
    <div class="phone">916 555 0148</div>
    <div class="addr">4820 Amberline Way #210<br>Rancho Verde, CA 95600</div>
    <div class="hours">8:00am to 4:00pm</div>
  </div>
  <div class="abs view-map">View map...</div>
  <div class="abs news"><h5>Subscribe to our Newsletter</h5><p>Receive regular exclusive offers and news</p></div>
  <div class="abs email"><div class="ico"><svg width="13" height="10" viewBox="0 0 13 10"><rect width="13" height="10" rx="1" fill="#777"/><path d="M0.5 0.8l6 4.5 6-4.5" fill="none" stroke="#fff"/></svg></div><span>name@domain.com</span></div>
  <div class="abs subscribe">Subscribe</div>
  <div class="abs copyright">Copyright © 2013 · All Rights Reserved</div>
  <div class="abs foot-follow">Follow us:
    <div class="social"><span><i></i>Chatterbook</span></div>
    <div class="social"><span><i></i>chirpnet</span></div>
  </div>
</footer>

</body>
</html>
```